Brightmark Power website design

Electrical contractor in Perth that services the domestic and commercial markets. our services include but not limited to:

New Home Installations and Design
Commercial Shop Fit Outs
Rewires
Renovations
Switchboard Upgrades
Kitchen and Bathroom Renovations
RCD'S (Safety Switches)
Smoke Alarms
Power points
Security Lighting
Energy Efficient LED Lighting Designs
Garden Lighting
Downlights
General Electrical Maintenance
TV and Phone Points
Home Theatre Installs
Safety Certificates
24hr Call out service
Electric Hot Water Units
Credit cards accepted

www.sociabook.example/brightmarkpower

Contractor

5+ page

Sans Serif

acd037
fbee3e

• contact page, services page, about us, careers page, somewhere I can put some testimonials, somewhere potential clients can book our services online, on the homepage somewhere showing that we can provide 24/7 emergency service
• icon stating that we accept all major credit cards

```html
<!DOCTYPE html>
<html lang="en">
<head>
<meta charset="utf-8">
<title>Brightmark Power</title>
<link href="https://fonts.googleapis.com/css2?family=Cousine&family=Open+Sans+Condensed:wght@300&family=Roboto:wght@500;700&display=swap" rel="stylesheet">
<style>
  :root {
    --lime: #e3dd33;
    --lime-bright: #fbee3e;
    --page: #f4f4f4;
    --panel: #404040;
    --white: #ffffff;
    --ink: #333333;
    --blue: #3ab0e0;
    --red: #f0545a;
    --green: #4caf50;
  }
  * { box-sizing: border-box; margin: 0; padding: 0; }
  html, body { width: 1200px; height: 900px; overflow: hidden; }
  body { background: var(--page); font-family: "Roboto", sans-serif; position: relative; }

  .topbar { position: absolute; left: 0; top: 0; width: 1200px; height: 56px; background: var(--lime); }
  .topbar-line { position: absolute; left: 115px; top: 0; width: 957px; height: 1px; background: var(--white); }

  .site { position: absolute; left: 160px; top: 0; width: 829px; height: 900px; background: var(--white); }

  .header { position: relative; height: 56px; background: var(--lime); display: flex; align-items: center; justify-content: space-between; padding: 0 14px 0 12px; }
  .brand { display: flex; align-items: center; gap: 10px; color: var(--white); font-family: "Open Sans Condensed", sans-serif; font-weight: 300; font-size: 21px; }
  .brand-dot { width: 22px; height: 22px; border-radius: 50%; border: 2px solid var(--white); }
  .nav { display: flex; gap: 13px; }
  .nav a { color: var(--white); text-decoration: none; font-family: "Cousine", monospace; font-size: 11.5px; }

  .hero { position: relative; height: 331px; background:
      linear-gradient(180deg, #3a2a18 0%, #8a4a12 18%, #4a4a22 38%, #6b6a3a 58%, #8a6a3a 72%, #3e3a1a 100%); }
  .hero-caption { position: absolute; left: 16px; top: 265px; width: 290px; height: 39px; background: var(--lime); border-radius: 6px; display: flex; align-items: center; padding-left: 10px; font-family: "Open Sans Condensed", sans-serif; font-weight: 300; font-size: 15px; color: var(--ink); }
  .hero-dots { position: absolute; left: 386px; top: 306px; display: flex; gap: 9px; }
  .hero-dots span { width: 13px; height: 13px; border-radius: 50%; background: var(--lime); }
  .hero-dots span.active { border: 3px solid var(--lime); background: radial-gradient(circle, #555 0 2px, var(--lime) 2.5px); }

  .features { height: 159px; background: var(--panel); display: flex; }
  .feature { flex: 1; display: flex; flex-direction: column; align-items: center; padding-top: 30px; }
  .feature svg { width: 42px; height: 42px; }
  .feature p { margin-top: 30px; font-size: 12px; font-weight: 700; }
  .feature.online { color: var(--blue); }
  .feature.emergency { color: var(--red); }
  .feature.cards { color: var(--green); }

  .story { position: absolute; left: 0; width: 829px; }
  .story-photo { position: absolute; width: 207px; border-radius: 50% / 50%; }
  .story-text { position: absolute; font-size: 14px; font-weight: 700; line-height: 18px; color: var(--ink); }
  .story-one { top: 575px; }
  .story-one .story-photo { left: 23px; top: 0; height: 138px; border-radius: 70px; background: linear-gradient(135deg, #e8e4dc, #7fa6b8 55%, #f0f0f0); }
  .story-one .story-text { left: 275px; top: 15px; width: 470px; }
  .story-two { top: 730px; }
  .story-two .story-photo { left: 552px; top: 0; height: 150px; border-radius: 75px; background: linear-gradient(135deg, #b88858, #e8dcc8 50%, #a87848); }
  .story-two .story-text { left: 23px; top: 15px; width: 500px; }
  .story-three-photo { position: absolute; left: 55px; top: 896px; width: 140px; height: 40px; border-radius: 70px; background: #b08a5a; }
</style>
</head>
<body>
  <div class="topbar"><div class="topbar-line"></div></div>
  <div class="site">
    <header class="header">
      <div class="brand"><span class="brand-dot"></span>Brightmark Power</div>
      <nav class="nav">
        <a href="#">Home</a><a href="#">Contact</a><a href="#">About</a><a href="#">Careers</a><a href="#">Testimonials</a>
      </nav>
    </header>

    <section class="hero" role="img" aria-label="Photograph of a river at sunset with trees and reeds under an orange sky">
      <div class="hero-caption">Lorem ipsum dolor sit amet, consectetuer adipiscing elit</div>
      <div class="hero-dots"><span class="active"></span><span></span><span></span></div>
    </section>

    <section class="features">
      <div class="feature online">
        <svg viewBox="0 0 42 42" fill="none" stroke="currentColor" stroke-width="3"><circle cx="21" cy="21" r="17"/><ellipse cx="21" cy="21" rx="7" ry="17"/><line x1="4" y1="21" x2="38" y2="21"/></svg>
        <p>Book our services online</p>
      </div>
      <div class="feature emergency">
        <svg viewBox="0 0 42 42" fill="none" stroke="currentColor" stroke-width="3.5"><path d="M2 21 Q21 2 40 21 Q21 40 2 21 Z"/><circle cx="21" cy="21" r="6"/></svg>
        <p>24/7 Emergency service</p>
      </div>
      <div class="feature cards">
        <svg viewBox="0 0 42 42" fill="none" stroke="currentColor" stroke-width="3.5"><polyline points="4,22 15,33 38,9"/></svg>
        <p>We accept all major credit cards</p>
      </div>
    </section>

    <article class="story story-one">
      <div class="story-photo" role="img" aria-label="Photo of a person working at a desk with stationery and a mug"></div>
      <p class="story-text">Duis autem vel eum iriure dolor in hendrerit in vulputate velit esse molestie consequat.</p>
    </article>
    <article class="story story-two">
      <p class="story-text">Nam liber tempor cum soluta nobis eleifend option congue nihil imperdiet doming id quod mazim placerat facer possim assum.</p>
      <div class="story-photo" role="img" aria-label="Photo of a notepad and coloured pencils on a cork board"></div>
    </article>
    <div class="story-three-photo" role="img" aria-label="Photo for the next story"></div>
  </div>
</body>
</html>
```